Business card design needed

I need a business card for my new Food & Lifestyle Coaching business - "Bloomvale Food & Lifestlye Coaching"

i already have a logo and would like to have that incorporated into the business card, obviously.

i would like a design that says "fresh" and "funky" - my target market is female, aged 20-45 so i want something that will stand out to them when they see it.

My "Company Colour" is Apple Green
Updates

Thankyou to everyone who has submitted a design for my project. At this stage i have quite a large number of designs to chose from and with only a short time until my project closes i am focusing now on chosing from those i have already shortlisted so am unfortunately not considering any new desings.

Thankyou again for your interest in my project.

Target Market(s)

Female, Health Conscious (or looking to improve their health/lifestyle), aged between 20-45

Industry/Entity Type

Business

Contact Information for Business Card

Tamsin Corley
Ph: 0417382946
Email: eatwell@marovex.com

Requirements
Must have
• Must include my existing Logo
Nice to have
• Would be nice to incoirporate and appointment card on the back

```html
<!DOCTYPE html>
<html lang="en">
<head>
<meta charset="utf-8">
<title>Bloomvale Food &amp; Lifestlye Coaching – Business Card</title>
<link href="https://fonts.googleapis.com/css2?family=Mulish:wght@400;600;800&display=swap" rel="stylesheet">
<style>
  :root {
    --apple-green: #8cc63f;
    --apple-green-light: #a6d65c;
    --ink: #1e1e1e;
    --rule: #9a9a9a;
    --paper: #ffffff;
    --backdrop: #2b2b2b;
  }
  * { box-sizing: border-box; margin: 0; padding: 0; }
  html, body { width: 1200px; height: 900px; overflow: hidden; }
  body {
    background: var(--backdrop);
    font-family: "Mulish", sans-serif;
    color: var(--ink);
    display: flex;
    flex-direction: column;
    align-items: center;
    justify-content: center;
    gap: 56px;
  }
  .card {
    position: relative;
    width: 580px;
    height: 350px;
    background: var(--paper);
    overflow: hidden;
    box-shadow: 0 10px 30px rgba(0,0,0,.45);
  }

  /* ---------- appointment side ---------- */
  .appointment-band {
    position: absolute;
    inset: 0 0 auto 0;
    height: 150px;
    background: var(--apple-green);
    border-bottom: 6px solid var(--apple-green-light);
  }
  .brand {
    display: flex;
    align-items: center;
    gap: 10px;
  }
  .brand-dot {
    width: 22px; height: 22px;
    border-radius: 50%;
    background: var(--apple-green);
  }
  .brand-text { display: flex; flex-direction: column; line-height: 1; }
  .brand-name { font-size: 40px; font-weight: 600; letter-spacing: .5px; }
  .brand-tagline { font-size: 10px; font-weight: 600; margin-top: 4px; margin-left: 40px; }
  .appointment-band .brand {
    position: absolute; left: 40px; top: 46px; color: var(--paper);
  }
  .appointment-band .brand-dot { background: var(--paper); }

  .appointment-form {
    position: absolute;
    left: 40px; right: 40px; top: 176px;
    font-size: 10px;
    color: #555;
  }
  .form-row { display: flex; gap: 24px; margin-bottom: 14px; }
  .form-field { flex: 1; border-top: 1px solid var(--rule); padding-top: 3px; }
  .form-field.center { text-align: center; }
  .form-field.right { text-align: right; }
  .appointment-phone {
    position: absolute;
    right: 40px; bottom: 26px;
    font-size: 15px;
    font-weight: 600;
    letter-spacing: 11px;
    color: var(--ink);
  }

  /* ---------- contact side ---------- */
  .brand-decoration {
    position: absolute;
    left: 44px; top: 92px;
    width: 150px; height: 150px;
    border-radius: 50%;
    background: var(--apple-green);
  }
  .trail { position: absolute; inset: 0; }
  .contact-block {
    position: absolute;
    right: 34px; top: 40px;
    width: 300px;
  }
  .contact-block .brand { color: var(--ink); margin-bottom: 26px; }
  .contact-name { font-size: 29px; font-weight: 800; letter-spacing: -.5px; line-height: 1; }
  .contact-name .accent { color: var(--apple-green); }
  .contact-phone {
    font-size: 17px;
    padding: 4px 0 6px 40px;
    border-bottom: 2px dotted var(--apple-green);
  }
  .contact-email { font-size: 17px; font-weight: 800; margin-top: 10px; }
  .contact-email .accent { color: var(--apple-green); }
</style>
</head>
<body>

  <section class="card card-appointment" aria-label="Appointment card">
    <div class="appointment-band">
      <div class="brand">
        <span class="brand-dot"></span>
        <div class="brand-text">
          <span class="brand-name">Bloomvale</span>
          <span class="brand-tagline">Food &amp; Lifestlye Coaching</span>
        </div>
      </div>
    </div>
    <div class="appointment-form">
      <div class="form-row"><div class="form-field center">has an appointment on</div></div>
      <div class="form-row">
        <div class="form-field">day</div>
        <div class="form-field center">month</div>
        <div class="form-field right">date</div>
      </div>
      <div class="form-row"><div class="form-field center" style="flex:0 0 46%;margin:0 auto">time</div></div>
    </div>
    <div class="appointment-phone">0417382946</div>
  </section>

  <section class="card card-contact" aria-label="Contact card">
    <div class="brand-decoration" aria-hidden="true"></div>
    <svg class="trail" viewBox="0 0 580 350" aria-hidden="true">
      <path d="M150 250 C 170 300, 230 310, 300 290 S 460 250, 560 226"
            fill="none" stroke="var(--apple-green)" stroke-width="3"
            stroke-dasharray="0 7" stroke-linecap="round"/>
    </svg>
    <div class="contact-block">
      <div class="brand">
        <span class="brand-dot"></span>
        <div class="brand-text">
          <span class="brand-name">Bloomvale</span>
          <span class="brand-tagline">Food &amp; Lifestlye Coaching</span>
        </div>
      </div>
      <div class="contact-name">tamsin<span class="accent">corley</span></div>
      <div class="contact-phone">0417382946</div>
      <div class="contact-email"><span class="accent">eatwell</span>@marovex.com</div>
    </div>
  </section>

</body>
</html>
```